Re-design our Infographic White Paper

We've created an infographic out of a company white paper. This document was created to show how Live Webcasting is an effective investment for corporate communications. We need to use this document to bring in new clients and increase our bottom line.

Feedback has been that our current design is unorganized and busy. We would like a new design that groups facts, quotes, and slogans together instead of dispersed as they are now. We would like most of the information to stay on, if possible, just with a cleaner design. Our website is www.halvorcast.com where you can see our color palate of white, green, and blue. This will be for PRINT, not web.

Target Market(s)

Large corporate communication department heads looking for internal communication live streaming.

Industry/Entity Type

Videography

Font styles to use
Sans Serif

Colors
3176b5
acd036
ffffff
85acd3
cadf82

Requirements
Must have
• Must fit on a single front page. Must include quotes and "Reliable Return on Communication". Must include Halvorcast contact info. Must be in company color palatte
Nice to have
• We would like most of our copy and stats included. "Quality of Experience" and "Tracking Success" are supposed to be our headings. We want this to really pop, and the current design is crowded and sucks.
Should not have
• Avoid anything negative about having a bad experience with other companies.

```html
<!DOCTYPE html>
<html lang="en">
<head>
<meta charset="utf-8">
<title>Reliable Return on Communication – Halvorcast</title>
<link rel="stylesheet" href="https://fonts.googleapis.com/css2?family=Montserrat:wght@400;500;600;700;800&family=Raleway:ital,wght@0,400;0,500;1,300;1,400&display=swap">
<style>
  :root {
    --blue: #1f4fa0;
    --blue-dark: #17407f;
    --green: #a9c83a;
    --orange: #e65c2e;
    --ink: #2b2b2b;
    --muted: #9a9a9a;
    --rule: #c8c8c8;
    --white: #ffffff;
  }
  * { box-sizing: border-box; margin: 0; padding: 0; }
  html, body { width: 960px; height: 1200px; overflow: hidden; background: var(--white); }
  body { position: relative; font-family: "Raleway", Arial, sans-serif; color: var(--ink); }
  .abs { position: absolute; }

  /* Header */
  .hero { left: 0; top: 0; width: 960px; height: 268px; background: var(--blue); }
  .hero-art { left: 44px; top: 36px; width: 346px; height: 206px; border-radius: 6px;
    background: linear-gradient(135deg, #3b6cc0 0%, #f3c6a9 55%, #e9edf2 100%); opacity: .9; }
  .hero-title { left: 441px; top: 64px; font-family: "Montserrat", sans-serif; font-weight: 700;
    color: var(--white); font-size: 36px; letter-spacing: 2.5px; line-height: 1; }
  .hero-title .accent { display: block; color: var(--green); font-size: 45px; font-weight: 800; letter-spacing: 2px; margin-top: 6px; }
  .hero-sub { left: 515px; top: 176px; color: var(--white); font-family: "Montserrat", sans-serif; font-size: 18px; line-height: 22px; font-weight: 400; }
  .hero-sub strong { font-weight: 600; }
  .clapper { left: 452px; top: 176px; }

  .stripe { left: 0; width: 960px; height: 12px;
    background: repeating-linear-gradient(-60deg, var(--green) 0 9px, transparent 9px 16px); }

  /* Section headings */
  .section-title { font-family: "Montserrat", sans-serif; font-weight: 800; color: var(--blue);
    font-size: 27px; line-height: 28px; letter-spacing: 1.5px; }

  .quote { background: var(--orange); color: var(--white); font-style: italic; font-weight: 300;
    font-size: 12px; line-height: 16px; padding: 10px 12px; }
  .quote::after { content: ""; position: absolute; right: 18px; bottom: -26px; width: 0; height: 0;
    border-left: 34px solid transparent; border-top: 26px solid var(--orange); }

  .years-bar { left: 236px; top: 430px; width: 592px; height: 78px; background: var(--blue); border-radius: 0 10px 10px 0;
    color: var(--white); font-family: "Montserrat", sans-serif; font-weight: 600; font-size: 17.5px; line-height: 25px;
    padding: 14px 0 0 26px; white-space: nowrap; z-index: 1; }
  .years-badge { left: 130px; top: 408px; width: 122px; height: 122px; border-radius: 50%; background: var(--white);
    border: 6px solid var(--blue); text-align: center; font-family: "Montserrat", sans-serif; color: var(--blue); z-index: 2; }
  .years-badge .lbl { display: block; font-size: 14px; margin-top: 20px; font-weight: 400; line-height: 16px; }
  .years-badge .num { display: block; font-size: 52px; font-weight: 700; line-height: 46px; letter-spacing: -2px; }
  .years-badge .unit { position: absolute; left: 62px; top: 84px; font-size: 9px; font-weight: 700; white-space: nowrap; }

  .desk-art { left: 44px; top: 548px; width: 222px; height: 142px; border-radius: 4px;
    background: linear-gradient(160deg, #c7cdd6 0%, #9aa5b4 60%, #2d3a55 100%); }

  .feature { text-align: center; font-size: 13px; line-height: 18.5px; color: var(--ink); }
  .vrule { width: 1px; background: var(--rule); }
  .dash-rule { left: 31px; top: 718px; width: 895px; border-top: 3px dashed var(--green); }

  .chart-art { left: 54px; top: 833px; width: 182px; height: 198px; border-radius: 4px;
    background: linear-gradient(150deg, #dfe6d3 0%, #f2f2f2 45%, #e65c2e 80%, #2b2b2b 100%); opacity: .85; }
  .lead { left: 256px; top: 845px; font-family: "Montserrat", sans-serif; font-size: 15.5px; line-height: 21px; color: var(--ink); }
  .hrule { left: 256px; top: 908px; width: 658px; height: 1px; background: var(--rule); }
  .stat { font-family: "Montserrat", sans-serif; font-size: 12.5px; line-height: 18px; color: var(--ink); }

  /* Footer */
  .brand { left: 52px; top: 1123px; display: flex; align-items: center; gap: 14px; }
  .brand-mark { width: 30px; height: 30px; background: var(--blue); }
  .brand-name { font-family: "Montserrat", sans-serif; font-weight: 600; color: var(--blue); font-size: 14px; letter-spacing: 6px; }
  .contact { top: 1127px; display: flex; align-items: center; gap: 10px; font-family: "Montserrat", sans-serif;
    color: var(--blue); font-size: 18px; }
  .contact.phone { font-weight: 700; }
</style>
</head>
<body>

<header>
  <div class="abs hero"></div>
  <div class="abs hero-art" role="img" aria-label="Illustration of a smiling presenter beside a monitor and phone streaming video, with audience avatars and chat bubbles"></div>
  <h1 class="abs hero-title">RELIABLE RETURN ON<span class="accent">COMMUNICATION</span></h1>
  <svg class="abs clapper" width="52" height="46" viewBox="0 0 52 46" aria-hidden="true">
    <rect x="2" y="14" width="48" height="30" rx="3" fill="#3a3a3a"/>
    <rect x="2" y="4" width="48" height="8" fill="#fff"/>
    <path d="M6 4h6l-4 8H2zM18 4h6l-4 8h-6zM30 4h6l-4 8h-6zM42 4h6l-4 8h-6z" fill="#e65c2e"/>
    <rect x="18" y="22" width="16" height="13" rx="2" fill="#e65c2e"/>
    <path d="M23 25l6 3.5-6 3.5z" fill="#fff"/>
  </svg>
  <p class="abs hero-sub"><strong>Professional Live Webcasting</strong> solutions<br>for effective messaging in your organization</p>
</header>

<div class="abs stripe" style="top:273px"></div>

<section class="quality">
  <svg class="abs" style="left:45px;top:308px" width="76" height="84" viewBox="0 0 76 84" aria-hidden="true">
    <polygon points="38,3 73,22 73,62 38,81 3,62 3,22" fill="#fff" stroke="#a9c83a" stroke-width="4"/>
    <circle cx="38" cy="38" r="16" fill="none" stroke="#1f4fa0" stroke-width="4"/>
    <path d="M38 29l3 6 6 .8-4.5 4.3 1 6.2-5.5-3-5.5 3 1-6.2-4.5-4.3 6-.8z" fill="#1f4fa0"/>
    <path d="M30 52l-4 14 6-3 3 5 3-10zM46 52l4 14-6-3-3 5-3-10z" fill="#1f4fa0"/>
  </svg>
  <h2 class="abs section-title" style="left:135px;top:324px">QUALITY OF<br>EXPERIENCE</h2>

  <blockquote class="abs quote" style="left:353px;top:321px;width:231px;height:62px">“This was an awesome town hall. The energy of the meeting made me feel like I was sitting in the room. :-) ”</blockquote>
  <blockquote class="abs quote" style="left:613px;top:321px;width:306px;height:62px">“Thank you so much for providing this webcast! It’s the next best thing to being there and bridges that gap so much more than an audio conference.”</blockquote>

  <div class="abs years-bar">Halvorcast provides a Reliable, Repeatable Experience,<br>so you can just focus on your messaging.</div>
  <div class="abs years-badge"><span class="lbl">Combined</span><span class="num">50</span><span class="unit">YEARS</span></div>

  <div class="abs desk-art" role="img" aria-label="Isometric illustration of a businessman working at a desk with a laptop and binders"></div>

  <svg class="abs" style="left:372px;top:528px" width="62" height="68" viewBox="0 0 62 68" aria-hidden="true">
    <g stroke="#e65c2e" stroke-width="2" fill="none">
      <path d="M8 22L22 6 42 4 56 22 52 44 30 38 8 22 30 20 42 4M22 6l8 14 22 24M56 22L30 20 30 38M8 22l4 20 18-4"/>
    </g>
    <g fill="#e65c2e"><circle cx="8" cy="22" r="4"/><circle cx="22" cy="6" r="4"/><circle cx="42" cy="4" r="4"/><circle cx="56" cy="22" r="4"/><circle cx="52" cy="44" r="4"/><circle cx="12" cy="42" r="4"/></g>
    <circle cx="31" cy="40" r="7" fill="#1f4fa0"/>
    <path d="M19 66c0-10 5-16 12-16s12 6 12 16z" fill="#1f4fa0"/>
  </svg>
  <p class="abs feature" style="left:285px;top:614px;width:232px">Employees Expect rich media experiences and interactive meetings. Build Trust and Transparency with Live Video Webcasts.</p>

  <div class="abs vrule" style="left:544px;top:519px;height:169px"></div>

  <svg class="abs" style="left:608px;top:530px" width="68" height="56" viewBox="0 0 68 56" aria-hidden="true">
    <g fill="none" stroke="#1f4fa0" stroke-width="2.5"><path d="M22 20a12 12 0 0 1 24 0M16 20a18 18 0 0 1 36 0"/></g>
    <circle cx="34" cy="20" r="6" fill="#1f4fa0"/>
    <path d="M22 54V38c0-6 5-10 12-10s12 4 12 10v16z" fill="#1f4fa0"/>
    <circle cx="11" cy="32" r="5" fill="#e65c2e"/><path d="M0 54V46c0-5 5-8 11-8s10 3 10 8v8z" fill="#e65c2e"/>
    <circle cx="57" cy="32" r="5" fill="#e65c2e"/><path d="M47 54V46c0-5 5-8 10-8s11 3 11 8v8z" fill="#e65c2e"/>
  </svg>
  <p class="abs feature" style="left:568px;top:614px;width:146px">Ensure an identical experience for all teammates to enchance message clarity.</p>

  <div class="abs vrule" style="left:738px;top:519px;height:169px"></div>

  <svg class="abs" style="left:806px;top:514px" width="92" height="76" viewBox="0 0 92 76" aria-hidden="true">
    <rect x="2" y="26" width="56" height="40" fill="none" stroke="#e65c2e" stroke-width="3.5"/>
    <path d="M22 36l16 10-16 10z" fill="#e65c2e"/>
    <rect x="2" y="68" width="56" height="4" fill="#e65c2e"/>
    <path d="M44 24l26-18 6 26-24-2z" fill="#1f4fa0"/>
    <rect x="36" y="20" width="10" height="14" rx="2" fill="#1f4fa0" transform="rotate(-25 41 27)"/>
    <path d="M80 8l8-6M82 18h8M80 28l8 4" stroke="#1f4fa0" stroke-width="2.5"/>
  </svg>
  <p class="abs feature" style="left:770px;top:616px;width:150px">Engage your audience with edited videos, interactive Q&amp;A sessions, and live polling.</p>
</section>

<div class="abs dash-rule"></div>

<section class="tracking">
  <svg class="abs" style="left:45px;top:743px" width="76" height="84" viewBox="0 0 76 84" aria-hidden="true">
    <polygon points="38,3 73,22 73,62 38,81 3,62 3,22" fill="#fff" stroke="#a9c83a" stroke-width="4"/>
    <rect x="18" y="46" width="7" height="14" fill="#1f4fa0"/><rect x="28" y="40" width="7" height="20" fill="#1f4fa0"/>
    <rect x="38" y="34" width="7" height="26" fill="#1f4fa0"/><rect x="48" y="28" width="7" height="32" fill="#1f4fa0"/>
    <path d="M18 38l12-8 10 4 14-12" fill="none" stroke="#1f4fa0" stroke-width="2.5"/>
    <circle cx="30" cy="30" r="2.5" fill="#fff" stroke="#1f4fa0" stroke-width="2"/><circle cx="54" cy="22" r="2.5" fill="#fff" stroke="#1f4fa0" stroke-width="2"/>
  </svg>
  <h2 class="abs section-title" style="left:135px;top:758px">TRACKING<br>SUCCESS</h2>

  <blockquote class="abs quote" style="left:520px;top:760px;width:396px;height:62px">“[The webcast] gives us a chance to become familiar w/alternative leadership, and programs and pilots and strategies and successes that we would never be exposed to outside of this Town Hall.”</blockquote>

  <div class="abs chart-art" role="img" aria-label="Isometric illustration of a presenter pointing at growth charts on display boards"></div>

  <p class="abs lead">Get Valuable Data for return on communication.<br>Webcasting statistics show your level of Employee Engagement.</p>
  <div class="abs hrule"></div>

  <svg class="abs" style="left:268px;top:933px" width="56" height="50" viewBox="0 0 56 50" aria-hidden="true">
    <rect x="2" y="2" width="52" height="34" fill="none" stroke="#1f4fa0" stroke-width="3"/>
    <rect x="24" y="38" width="8" height="6" fill="#1f4fa0"/><rect x="16" y="44" width="24" height="4" fill="#1f4fa0"/>
    <g fill="#e65c2e"><rect x="9" y="24" width="4" height="8"/><rect x="16" y="18" width="4" height="14"/><rect x="23" y="22" width="4" height="10"/><rect x="30" y="12" width="4" height="20"/><rect x="37" y="16" width="4" height="16"/><rect x="44" y="10" width="4" height="22"/></g>
  </svg>
  <p class="abs stat" style="left:341px;top:942px">Consistently see viewership<br>exceed expectations</p>

  <svg class="abs" style="left:268px;top:1009px" width="54" height="46" viewBox="0 0 54 46" aria-hidden="true">
    <path d="M20 2a18 16 0 1 1-10 30l-8 6 3-10A18 16 0 0 1 20 2z" fill="#1f4fa0"/>
    <path d="M14 16h4v10h-4zM19 16l4-7c2 0 3 1 3 3l-1 4h5c1.5 0 2.5 1.3 2 3l-2 6c-.4 1-1 1-2 1h-9z" fill="#fff"/>
    <path d="M40 22a13 11 0 1 1-6 20l-6 4 2-7a13 11 0 0 1 10-17z" fill="#fff" stroke="#e65c2e" stroke-width="3"/>
  </svg>
  <p class="abs stat" style="left:341px;top:1025px">Surveys and Feedback</p>

  <div class="abs vrule" style="left:552px;top:927px;height:135px"></div>

  <svg class="abs" style="left:603px;top:930px" width="58" height="58" viewBox="0 0 58 58" aria-hidden="true">
    <circle cx="29" cy="29" r="28" fill="#1f4fa0"/>
    <path d="M29 29V1a28 28 0 0 1 8.6 1.35z" fill="#e65c2e"/>
  </svg>
  <p class="abs stat" style="left:684px;top:942px">95% reach across your entire<br>organization simultaneously</p>

  <svg class="abs" style="left:602px;top:1009px" width="62" height="46" viewBox="0 0 62 46" aria-hidden="true">
    <rect x="6" y="2" width="50" height="34" rx="2" fill="none" stroke="#1f4fa0" stroke-width="3.5"/>
    <path d="M1 40h60l-3 4H4z" fill="#1f4fa0"/>
    <path d="M26 11l12 8-12 8z" fill="#e65c2e"/>
  </svg>
  <p class="abs stat" style="left:684px;top:1020px">Your video meetings become a<br>must watch event</p>
</section>

<div class="abs stripe" style="top:1088px"></div>

<footer>
  <div class="abs brand"><span class="brand-mark"></span><span class="brand-name">HALVORCAST</span></div>
  <div class="abs contact phone" style="left:422px">
    <svg width="22" height="22" viewBox="0 0 24 24" aria-hidden="true"><path d="M6.6 2.5l3 3.2-2 2.6c1.2 2.8 3.3 4.9 6.1 6.1l2.6-2 3.2 3-1.7 3.6C11 19.3 4.7 13 4.2 6.2z" fill="none" stroke="#e65c2e" stroke-width="1.8" stroke-linejoin="round"/></svg>
    <span>555.204.7730</span>
  </div>
  <div class="abs contact" style="left:667px">
    <svg width="22" height="22" viewBox="0 0 24 24" aria-hidden="true"><g fill="none" stroke="#e65c2e" stroke-width="1.8"><circle cx="12" cy="12" r="9.5"/><ellipse cx="12" cy="12" rx="4.5" ry="9.5"/><path d="M2.5 12h19M4 7h16M4 17h16"/></g></svg>
    <span>www.halvorcast.com</span>
  </div>
</footer>

</body>
</html>
```